Redesign the Eshop of a gift shop

We want to redesign the front page, the category page and the product page of our Eshop that sells gifts.
I am thinking not to reveal the url of the eshop as i don't want you to get influenced. Lets call the Eshop "PresentNook.com"
I will list the brands that we resell so you understand what we are selling,
Vorelli-https://www.vorelli-example.com/
Brimworth-https://brimworth-example.com/
Pandol - https://pandol-example.com/
Quiet Meadow - https://www.quietmeadow-example.com/
Fellow's Toolchest - https://fellowstoolchest-example.com/
Paperloft ink - https://paperloftink-example.com/
Pretzel - https://pretzelofficial-example.com/
We also sell toys for adults like backgamon, chess, playing cards, board games.
The problem is that many eshops sell these and thats why i would like the design to have a different approach, more fresh, not seen before.
I am also thinking of something playfull, happy, but warm at the same time.
Please note that our logo is black & white but feel free to play with any color/s you like in your website design. We might eventually even adjust the logo colors, or you can provide a pallete that suites a black and white logo
Let me know if you have any questions!
Target Market(s)
Age: 20-50, Gender: Also men but mostly women, Income: Moderate to high, Interests and Lifestyle: Customers who value sentimentality, personal connection, and thoughtful gestures, Relationship Status: Those in relationships or with larger families
Number of Pages Required
3 page
Look and feel
Each slider illustrates characteristics of the customer's brand and the style your logo design should communicate.

```html
<!DOCTYPE html>
<html lang="en">
<head>
<meta charset="utf-8">
<title>PresentNook – Garden Enamel Mug 500ml</title>
<link href="https://fonts.googleapis.com/css2?family=Inter:wght@400;500;600;700&family=Plus+Jakarta+Sans:wght@400;500;600;700&display=swap" rel="stylesheet">
<style>
:root{
  --ink:#1b1b1b;
  --text:#2a2a2a;
  --muted:#7a7a7a;
  --line:#e8e3dc;
  --soft:#f5f2ee;
  --cream:#fffdfa;
  --accent:#ea6a2f;
  --star:#f4892a;
  --green:#1f5133;
  --white:#ffffff;
}
*{box-sizing:border-box;margin:0;padding:0}
html,body{width:1200px;height:2848px;overflow:hidden;background:var(--cream)}
body{position:relative;font-family:"Inter",sans-serif;color:var(--text)}
.abs{position:absolute}
.jak{font-family:"Plus Jakarta Sans",sans-serif}
.star{width:16px;height:16px;fill:var(--star);vertical-align:middle}

/* header */
.nav a{position:absolute;top:39px;font-size:14px;color:var(--ink);text-decoration:none;font-weight:500}
.logo{position:absolute;left:500px;top:30px;width:200px;font-size:24px;letter-spacing:.5px;color:var(--ink);font-weight:500;display:flex;align-items:center;gap:8px;justify-content:center}
.logo i{display:block;width:11px;height:11px;background:var(--ink)}
.search{left:834px;top:27px;width:168px;height:39px;border:1px solid var(--line);border-radius:20px;font-size:12px;color:#9a9a9a;display:flex;align-items:center;gap:8px;padding-left:12px;background:var(--white)}
.cart{left:1011px;top:27px;width:39px;height:39px;border:1px solid var(--line);border-radius:50%;display:flex;align-items:center;justify-content:center;background:var(--white)}
.login{left:1057px;top:27px;width:70px;height:39px;border:1px solid var(--accent);border-radius:20px;color:var(--accent);font-size:12px;display:flex;align-items:center;justify-content:center}

.crumbs{left:99px;top:125px;font-size:12.5px;font-family:"Plus Jakarta Sans",sans-serif;display:flex;gap:10px;color:var(--accent)}
.crumbs b{font-weight:500;color:var(--ink)}
.crumbs span.sep{color:var(--muted)}

/* gallery */
.hero{left:99px;top:170px;width:485px;height:381px;border-radius:8px;background:radial-gradient(circle at 50% 48%,#e6e3dc 0,#dedad2 28%,#f3f1ed 52%)}
.arrow{width:36px;height:36px;border-radius:50%;background:#d9d6d0;display:flex;align-items:center;justify-content:center}
.thumb{top:565px;width:111px;height:110px;border-radius:6px;background:var(--soft);display:flex;align-items:center;justify-content:center}
.thumb.on{border:1.5px solid var(--green)}
.thumb div{width:72px;height:72px;border-radius:4px}

/* info */
.title{font-size:28px;font-weight:600;color:var(--ink)}
.meta{font-size:12.5px;color:#555;display:flex;align-items:center;gap:6px}
.meta .dot{width:3px;height:3px;border-radius:50%;background:#bbb}
.price{left:619px;top:264px;font-size:24px;font-weight:700;color:var(--accent)}
.desc{font-size:13.5px;line-height:20px;color:var(--muted)}
.hr{height:1px;background:var(--line)}
.label{font-size:13px;color:#444}
.select{top:493px;height:37px;width:117px;border:1px solid var(--line);border-radius:5px;font-size:12px;color:var(--ink);display:flex;align-items:center;justify-content:space-between;padding:0 14px;background:var(--white)}
.btn{top:573px;height:44px;width:216px;border-radius:5px;font-family:"Plus Jakarta Sans",sans-serif;font-size:14px;font-weight:700;display:flex;align-items:center;justify-content:center;gap:8px}
.btn.buy{left:619px;background:var(--green);color:#fff}
.btn.add{left:847px;border:1.5px solid var(--green);color:var(--green);background:var(--white)}

/* tabs */
.tabs{left:99px;top:724px;width:995px;height:39px;border-bottom:1px solid var(--line);display:flex;font-size:14px;color:#888}
.tabs span{padding:8px 20px 0}
.tabs .on{color:var(--green);font-weight:600;border-bottom:2px solid var(--green)}

.h3{font-family:"Plus Jakarta Sans",sans-serif;font-size:16px;font-weight:700;color:var(--ink)}

/* summary */
.summary{left:99px;top:1015px;width:995px;height:188px;border:1px solid var(--line);border-radius:8px;background:var(--white)}
.ring{left:119px;top:1035px;width:70px;height:70px;border:3px solid var(--star);border-radius:50%;display:flex;align-items:center;justify-content:center;font-family:"Plus Jakarta Sans",sans-serif;font-weight:700;font-size:17px}
.row{left:408px;width:660px;display:flex;align-items:center;font-family:"Plus Jakarta Sans",sans-serif;font-size:13px;color:var(--ink)}
.row .lab{width:49px;display:flex;gap:4px;align-items:center}
.row .bar{width:555px;height:5px;border-radius:3px;background:var(--line);margin-left:10px;position:relative;overflow:hidden}
.row .bar i{position:absolute;left:0;top:0;bottom:0;background:var(--accent);border-radius:3px}
.row .n{margin-left:20px;color:var(--ink)}

/* filter */
.filter{left:99px;top:1222px;width:231px;height:487px;border:1px solid var(--line);border-radius:8px;padding:0 19px;background:var(--white)}
.fhead{font-family:"Plus Jakarta Sans",sans-serif;font-size:13px;font-weight:700;color:var(--ink)}
.chk{display:flex;align-items:center;gap:9px;font-size:12.5px;color:#888;font-family:"Plus Jakarta Sans",sans-serif}
.chk i{width:18px;height:18px;border:1.5px solid #ccc;border-radius:4px;display:block}
.chk .s{display:flex;align-items:center;gap:3px;color:var(--star)}

/* reviews */
.chip{top:1258px;height:37px;border:1px solid var(--line);border-radius:5px;font-family:"Plus Jakarta Sans",sans-serif;font-size:11.5px;font-weight:500;color:var(--ink);display:flex;align-items:center;justify-content:center;background:var(--white)}
.chip.on{border-color:var(--accent);color:var(--accent)}
.review{left:363px;width:731px;height:175px;border-bottom:1px solid var(--line);font-family:"Plus Jakarta Sans",sans-serif}
.review .stars{position:absolute;top:0;display:flex;gap:4px}
.review .t{position:absolute;top:28px;font-size:14px;font-weight:700;color:var(--ink)}
.review .d{position:absolute;top:53px;font-size:12px;color:#9a9a9a}
.review .who{position:absolute;top:83px;display:flex;align-items:center;gap:11px;font-size:13px;font-weight:500;color:var(--ink)}
.review .who i{width:26px;height:26px;border-radius:50%;display:block}
.vote{position:absolute;top:75px;height:40px;border:1px solid var(--line);border-radius:5px;display:flex;align-items:center;justify-content:center;gap:8px;font-size:12.5px;color:#555;background:var(--white)}
.vote.up{left:612px;width:66px}
.vote.dn{left:690px;width:41px}

.page{top:1993px;width:37px;height:37px;border:1px solid var(--line);border-radius:5px;font-size:11px;color:#555;display:flex;align-items:center;justify-content:center;font-family:"Plus Jakarta Sans",sans-serif;background:var(--white)}
.page.on{color:var(--accent)}

/* related */
.viewbtn{left:1000px;top:2111px;width:94px;height:33px;border:1.5px solid var(--green);border-radius:6px;color:var(--green);font-family:"Plus Jakarta Sans",sans-serif;font-size:12px;font-weight:700;display:flex;align-items:center;justify-content:center}
.card{top:2170px;width:234px;font-family:"Plus Jakarta Sans",sans-serif}
.card .ph{height:231px;background:var(--soft);border-radius:4px;position:relative}
.card .ph .img{position:absolute;left:42px;top:42px;width:149px;height:149px}
.card .heart{position:absolute;right:10px;top:10px;width:24px;height:24px;display:flex;align-items:center;justify-content:center}
.card .nm{margin-top:17px;display:flex;justify-content:space-between;font-size:15px;font-weight:700;color:var(--ink);white-space:nowrap}
.card .nm b{color:var(--accent)}
.card .loc{margin-top:8px;font-size:12px;color:#9a9a9a}
.card .rt{margin-top:8px;font-size:12.5px;color:#555;display:flex;align-items:center;gap:6px;padding-bottom:6px;border-bottom:1px solid var(--line)}

/* footer */
.flogo{left:63px;top:2588px;font-size:24px;font-weight:500;color:var(--ink);display:flex;align-items:center;gap:8px}
.flogo i{width:11px;height:11px;background:var(--ink);display:block}
.fdesc{left:63px;top:2640px;width:230px;font-size:13px;line-height:20px;color:#555}
.fh{font-size:20px;color:var(--ink)}
.fl{font-size:13.5px;color:#333;line-height:33px}
.pay{top:2616px;width:57px;height:44px;border:1px solid var(--line);border-radius:6px;font-size:11px;font-weight:700;color:var(--ink);display:flex;align-items:center;justify-content:center;background:var(--white)}
.copy{left:0;width:1200px;top:2772px;text-align:center;font-size:11.5px;color:#9a9a9a}
</style>
</head>
<body>
<svg width="0" height="0" style="position:absolute">
  <defs>
    <symbol id="st" viewBox="0 0 24 24"><path d="M12 2.5l2.9 6.1 6.6.8-4.9 4.6 1.3 6.6L12 17.3l-5.9 3.3 1.3-6.6L2.5 9.4l6.6-.8z"/></symbol>
    <symbol id="up" viewBox="0 0 24 24"><path d="M7 10v11H3V10zM7 10l4-8c1.7 0 3 1.3 3 3v4h5.5c1.2 0 2.1 1.1 1.9 2.3l-1.4 8A2 2 0 0 1 18 21H7" fill="none" stroke="currentColor" stroke-width="1.6" stroke-linejoin="round"/></symbol>
    <symbol id="heart" viewBox="0 0 24 24"><path d="M12 20s-7-4.4-7-10a4 4 0 0 1 7-2.6A4 4 0 0 1 19 10c0 5.6-7 10-7 10z" fill="none" stroke="#222" stroke-width="1.6"/></symbol>
  </defs>
</svg>

<!-- header -->
<nav class="nav">
  <a style="left:66px">Home</a><a style="left:144px">Product</a><a style="left:234px">Blog</a><a style="left:302px">Contact Us</a>
</nav>
<div class="logo"><i></i>PresentNook</div>
<div class="abs search"><svg width="16" height="16" viewBox="0 0 24 24"><circle cx="11" cy="11" r="7" fill="none" stroke="#333" stroke-width="2"/><path d="M16 16l5 5" stroke="#333" stroke-width="2"/></svg>Search...</div>
<div class="abs cart"><svg width="16" height="16" viewBox="0 0 24 24"><path d="M5 8h14l-1.5 12h-11z" fill="#333"/><path d="M9 8V6a3 3 0 0 1 6 0v2" fill="none" stroke="#333" stroke-width="2"/></svg></div>
<div class="abs login">Login</div>

<div class="abs crumbs"><span>Home</span><span class="sep">›</span><span>Home &amp; Garden</span><span class="sep">›</span><span>Mugs &amp; Cups</span><span class="sep">›</span><b>Garden Enamel Mug 500ml</b></div>

<!-- gallery -->
<div class="abs hero" role="img" aria-label="White enamel mug with gardening spade print"></div>
<div class="abs arrow" style="left:113px;top:343px"><svg width="14" height="14" viewBox="0 0 24 24"><path d="M15 5l-7 7 7 7" fill="none" stroke="#222" stroke-width="2.2"/></svg></div>
<div class="abs arrow" style="left:535px;top:343px"><svg width="14" height="14" viewBox="0 0 24 24"><path d="M9 5l7 7-7 7" fill="none" stroke="#222" stroke-width="2.2"/></svg></div>
<div class="abs thumb on" style="left:99px"><div role="img" aria-label="Mug front view" style="background:#e2dfd8"></div></div>
<div class="abs thumb" style="left:224px"><div role="img" aria-label="Mug back view" style="background:#e4e1da"></div></div>
<div class="abs thumb" style="left:348px"><div role="img" aria-label="Mug top view" style="background:#d9d5cd"></div></div>
<div class="abs thumb" style="left:473px"><div role="img" aria-label="Mug in a gift box" style="background:#d3cdc3"></div></div>

<!-- info -->
<h1 class="abs title" style="left:619px;top:188px">Garden Enamel Mug 500ml</h1>
<div class="abs meta" style="left:619px;top:230px"><svg class="star"><use href="#st"/></svg>4.8<span class="dot"></span>1,238 Sold</div>
<div class="abs price">$139.99</div>
<p class="abs desc" style="left:619px;top:316px;width:485px">The perfect pour for any plant enthusiast! Our garden enamel mug features a clever design, with gardening tool illustrations and “The Ace of Spades” phrasing. An ideal gift for any gardener, this mug holds up to 16 fl oz. Product size: 4"L x 4"W x 3.5"HCapacity: 16 fl oz</p>
<div class="abs hr" style="left:619px;top:414px;width:475px"></div>
<div class="abs h3" style="left:619px;top:436px;font-size:14px">Product Variant:</div>
<div class="abs label" style="left:619px;top:468px">Size</div>
<div class="abs label" style="left:747px;top:468px">Color</div>
<div class="abs select" style="left:619px">500ml<svg width="10" height="10" viewBox="0 0 24 24"><path d="M5 9l7 7 7-7" fill="none" stroke="#222" stroke-width="2.5"/></svg></div>
<div class="abs select" style="left:747px">Cream<svg width="10" height="10" viewBox="0 0 24 24"><path d="M5 9l7 7 7-7" fill="none" stroke="#222" stroke-width="2.5"/></svg></div>
<div class="abs btn buy">Buy Now</div>
<div class="abs btn add"><svg width="18" height="18" viewBox="0 0 24 24"><path d="M2 4h3l2.5 11h11L21 7H6.5" fill="none" stroke="#1f5133" stroke-width="1.8"/><circle cx="9" cy="19" r="1.5" fill="#1f5133"/><circle cx="17" cy="19" r="1.5" fill="#1f5133"/></svg>Add to Cart</div>

<!-- tabs -->
<div class="abs tabs"><span class="on">Detail Product</span><span>Merchant</span><span>Reviews</span><span>Related Product</span></div>
<h2 class="abs title" style="left:99px;top:789px">Garden Enamel Mug 500ml</h2>
<p class="abs desc" style="left:99px;top:832px;width:880px">The perfect pour for any plant enthusiast! Our garden enamel mug features a clever design, with gardening tool illustrations and “The Ace of Spades” phrasing. An ideal gift for any gardener, this mug holds up to 16 fl oz.<br>Product size: 4"L x 4"W x 3.5"HCapacity: 16 fl oz</p>
<div class="abs hr" style="left:99px;top:945px;width:995px"></div>

<!-- reviews summary -->
<div class="abs h3" style="left:99px;top:974px">Product Reviews</div>
<div class="abs summary"></div>
<div class="abs ring">4.8</div>
<div class="abs" style="left:202px;top:1047px;display:flex;gap:4px"><svg class="star"><use href="#st"/></svg><svg class="star"><use href="#st"/></svg><svg class="star"><use href="#st"/></svg><svg class="star"><use href="#st"/></svg><svg class="star"><use href="#st"/></svg></div>
<div class="abs jak" style="left:202px;top:1074px;font-size:12.5px;color:#333">from 1,25k reviews</div>
<div class="abs row" style="top:1037px"><span class="lab">5.0<svg class="star" style="width:14px"><use href="#st"/></svg></span><span class="bar"><i style="width:84%"></i></span><span class="n">2823</span></div>
<div class="abs row" style="top:1069px"><span class="lab">4.0<svg class="star" style="width:14px"><use href="#st"/></svg></span><span class="bar"><i style="width:47.5%"></i></span><span class="n">38</span></div>
<div class="abs row" style="top:1101px"><span class="lab">3.0<svg class="star" style="width:14px"><use href="#st"/></svg></span><span class="bar"><i style="width:15%"></i></span><span class="n">4</span></div>
<div class="abs row" style="top:1132px"><span class="lab">2.0<svg class="star" style="width:14px"><use href="#st"/></svg></span><span class="bar"></span><span class="n">0</span></div>
<div class="abs row" style="top:1163px"><span class="lab">1.0<svg class="star" style="width:14px"><use href="#st"/></svg></span><span class="bar"></span><span class="n">0</span></div>

<!-- filter -->
<aside class="abs filter">
  <div class="abs h3" style="left:19px;top:22px;font-size:15px">Reviews Filter</div>
  <div class="abs hr" style="left:19px;top:55px;width:191px"></div>
  <div class="abs fhead" style="left:19px;top:78px">Rating</div>
  <svg class="abs" style="left:199px;top:82px" width="10" height="10" viewBox="0 0 24 24"><path d="M5 15l7-7 7 7" fill="none" stroke="#222" stroke-width="2.5"/></svg>
  <div class="abs chk" style="left:19px;top:106px"><i></i><span class="s"><svg class="star" style="width:14px"><use href="#st"/></svg><span style="color:#888">5</span></span></div>
  <div class="abs chk" style="left:19px;top:138px"><i></i><span class="s"><svg class="star" style="width:14px"><use href="#st"/></svg><span style="color:#888">4</span></span></div>
  <div class="abs chk" style="left:19px;top:169px"><i></i><span class="s"><svg class="star" style="width:14px"><use href="#st"/></svg><span style="color:#888">3</span></span></div>
  <div class="abs chk" style="left:19px;top:201px"><i></i><span class="s"><svg class="star" style="width:14px"><use href="#st"/></svg><span style="color:#888">2</span></span></div>
  <div class="abs chk" style="left:19px;top:232px"><i></i><span class="s"><svg class="star" style="width:14px"><use href="#st"/></svg><span style="color:#888">1</span></span></div>
  <div class="abs hr" style="left:19px;top:271px;width:191px"></div>
  <div class="abs fhead" style="left:19px;top:293px">Review Topics</div>
  <svg class="abs" style="left:199px;top:297px" width="10" height="10" viewBox="0 0 24 24"><path d="M5 15l7-7 7 7" fill="none" stroke="#222" stroke-width="2.5"/></svg>
  <div class="abs chk" style="left:19px;top:322px"><i></i>Product Quality</div>
  <div class="abs chk" style="left:19px;top:353px"><i></i>Seller Services</div>
  <div class="abs chk" style="left:19px;top:385px"><i></i>Product Price</div>
  <div class="abs chk" style="left:19px;top:416px"><i></i>Shipment</div>
  <div class="abs chk" style="left:19px;top:447px"><i></i>Match with Description</div>
</aside>

<!-- review list -->
<div class="abs h3" style="left:363px;top:1224px">Review Lists</div>
<div class="abs chip on" style="left:363px;width:85px">All Reviews</div>
<div class="abs chip" style="left:457px;width:127px">With Photo &amp; Video</div>
<div class="abs chip" style="left:593px;width:114px">With Description</div>

<section class="abs review" style="top:1322px">
  <div class="stars"><svg class="star"><use href="#st"/></svg><svg class="star"><use href="#st"/></svg><svg class="star"><use href="#st"/></svg><svg class="star"><use href="#st"/></svg><svg class="star"><use href="#st"/></svg></div>
  <div class="t">This is amazing product I have.</div><div class="d">July 2, 2020 03:29 PM</div>
  <div class="who"><i role="img" aria-label="Avatar of Darrell Steward" style="background:#8a7fc7"></i>Darrell Steward</div>
  <div class="vote up"><svg width="18" height="18" style="color:var(--accent)"><use href="#up"/></svg>128</div>
  <div class="vote dn"><svg width="18" height="18" style="transform:rotate(180deg)"><use href="#up"/></svg></div>
</section>
<section class="abs review" style="top:1497px">
  <div class="stars"><svg class="star"><use href="#st"/></svg><svg class="star"><use href="#st"/></svg><svg class="star"><use href="#st"/></svg><svg class="star"><use href="#st"/></svg><svg class="star"><use href="#st"/></svg></div>
  <div class="t">This is amazing product I have.</div><div class="d">July 2, 2020 1:04 PM</div>
  <div class="who"><i role="img" aria-label="Avatar of Darlene Robertson" style="background:#4a4a4a"></i>Darlene Robertson</div>
  <div class="vote up"><svg width="18" height="18"><use href="#up"/></svg>82</div>
  <div class="vote dn"><svg width="18" height="18" style="transform:rotate(180deg)"><use href="#up"/></svg></div>
</section>
<section class="abs review" style="top:1672px">
  <div class="stars"><svg class="star"><use href="#st"/></svg><svg class="star"><use href="#st"/></svg><svg class="star"><use href="#st"/></svg><svg class="star"><use href="#st"/></svg><svg class="star"><use href="#st"/></svg></div>
  <div class="t">This is amazing product I have.</div><div class="d">June 26, 2020 10:03 PM</div>
  <div class="who"><i role="img" aria-label="Avatar of Kathryn Murphy" style="background:#7fc3d6"></i>Kathryn Murphy</div>
  <div class="vote up"><svg width="18" height="18"><use href="#up"/></svg>9</div>
  <div class="vote dn"><svg width="18" height="18" style="transform:rotate(180deg)"><use href="#up"/></svg></div>
</section>
<section class="abs review" style="top:1847px;border-bottom:none">
  <div class="stars"><svg class="star"><use href="#st"/></svg><svg class="star"><use href="#st"/></svg><svg class="star"><use href="#st"/></svg><svg class="star"><use href="#st"/></svg><svg class="star"><use href="#st"/></svg></div>
  <div class="t">This is amazing product I have.</div><div class="d">July 7, 2020 10:14 AM</div>
  <div class="who"><i role="img" aria-label="Avatar of Ronald Richards" style="background:#8f8ad0"></i>Ronald Richards</div>
  <div class="vote up"><svg width="18" height="18"><use href="#up"/></svg>124</div>
  <div class="vote dn"><svg width="18" height="18" style="transform:rotate(180deg)"><use href="#up"/></svg></div>
</section>

<div class="abs page on" style="left:624px">1</div>
<div class="abs page" style="left:667px">2</div>
<div class="abs page" style="left:710px">...</div>
<div class="abs page" style="left:753px">19</div>
<svg class="abs" style="left:806px;top:2003px" width="16" height="16" viewBox="0 0 24 24"><path d="M9 5l7 7-7 7" fill="none" stroke="#ea6a2f" stroke-width="2.2"/></svg>

<!-- related -->
<div class="abs h3" style="left:99px;top:2118px">Related Product</div>
<div class="abs viewbtn">View Detail</div>

<article class="abs card" style="left:99px">
  <div class="ph"><div class="img" role="img" aria-label="Hand cleaning a black keyboard" style="background:linear-gradient(160deg,#d8b88e,#4a4540)"></div><span class="heart"><svg width="18" height="18"><use href="#heart"/></svg></span></div>
  <div class="nm">Keyboard Care Kit<b>$26</b></div><div class="loc">North Purwokerto</div>
  <div class="rt"><svg class="star" style="width:18px;height:18px"><use href="#st"/></svg>4.8<span style="color:#bbb">·</span>1,238 Sold</div>
</article>
<article class="abs card" style="left:353px">
  <div class="ph"><div class="img" role="img" aria-label="Hand lighting a campfire" style="background:linear-gradient(150deg,#3c2f27,#c9662a 60%,#2a231e)"></div><span class="heart"><svg width="18" height="18"><use href="#heart"/></svg></span></div>
  <div class="nm">Camp Fire Starter<b>$49</b></div><div class="loc">North Purwokerto</div>
  <div class="rt"><svg class="star" style="width:18px;height:18px"><use href="#st"/></svg>4.8<span style="color:#bbb">·</span>1,238 Sold</div>
</article>
<article class="abs card" style="left:607px">
  <div class="ph"><div class="img" role="img" aria-label="Dog beside a phone on a stand" style="background:linear-gradient(160deg,#efe3c4,#c4965f)"></div><span class="heart"><svg width="18" height="18"><use href="#heart"/></svg></span></div>
  <div class="nm">Pet Selfie Clip<b>$12</b></div><div class="loc">North Purwokerto</div>
  <div class="rt"><svg class="star" style="width:18px;height:18px"><use href="#st"/></svg>4.8<span style="color:#bbb">·</span>1,238 Sold</div>
</article>
<article class="abs card" style="left:861px">
  <div class="ph"><div class="img" role="img" aria-label="Three wire head massagers" style="background:linear-gradient(180deg,#ffffff,#ece8e2)"></div><span class="heart"><svg width="18" height="18"><use href="#heart"/></svg></span></div>
  <div class="nm">Head Massager Set<b>$48</b></div><div class="loc">North Purwokerto</div>
  <div class="rt"><svg class="star" style="width:18px;height:18px"><use href="#st"/></svg>4.8<span style="color:#bbb">·</span>1,238 Sold</div>
</article>

<!-- footer -->
<footer>
  <div class="abs flogo"><i></i>PresentNook</div>
  <p class="abs fdesc">Finding the perfect gift has never been easier. Browse thoughtful, playful presents for the people who matter most to you.</p>
  <div class="abs fh" style="left:376px;top:2578px">Menu</div>
  <div class="abs fl" style="left:376px;top:2612px">Men<br>Women<br>Order Tracking<br>Blog</div>
  <div class="abs fl" style="left:536px;top:2612px">FAQ<br>Privacy Policy<br>Term Of Conditions</div>
  <div class="abs fh" style="left:718px;top:2578px">Connect</div>
  <div class="abs fl" style="left:718px;top:2612px">Contact Us<br>Pictogram<br>Facefeed<br>Chirper</div>
  <div class="abs fh" style="left:852px;top:2578px">Payment Method</div>
  <div class="abs pay" style="left:852px">PayWell</div>
  <div class="abs pay" style="left:923px">TapPay</div>
  <div class="abs pay" style="left:995px">Mercard</div>
  <div class="abs pay" style="left:1066px">Vexa</div>
  <div class="abs copy">© 2022 PresentNook® Global Inc.</div>
</footer>
</body>
</html>
```